Business Card/Design Project for Personal Injury Lawyer

Personal Injury Attorney. I represent people who have been injured in accidents and are making money damage claims against the negligent party. As a personal injury attorney, I am a counselor, advisor, and legal representative to my clients. Clients want someone who is aggresssive yet professional.

More information about what I do an be found at www.vorlandlaw.example

Target Market(s)

General public.

Industry/Entity Type

Legal

Contact Information for Business Card

Need a new logo/brand image for b-cards, website, and letterhead/envelops. Looking for something original (no scales of justice or courthouse columns), yet classy and professional.

Here's what I'm thinking (but I'm always open to other ideas):

On the front, I would like my name (Colton R. Vorland), and underneath the words "Personal Injury Attorney." The background could be black, for example, and the lettering could be white or foil. I'm open to differnt colors, or even two colors. My name on the front side should pop.

And then on the back would be all my contact info, and maybe a logo or a slogan.

Here are two slogans I've come up with so far: 1. Fight for Full Value. 2. Steady Counsel When Harm Is Serious.

Requirements
Must have
• Something that identifys me as a personal injury attorney, such as the words Personal Injury Attorney (or Lawyer, or Law Firm, etc.).
Nice to have
• A style/image that can be used nicely on my website and on letterhead.
Should not have
• Tired, commonly used logos or symbols, such a scales of justice or courthouse columns.

```html
<!DOCTYPE html>
<html lang="en">
<head>
<meta charset="utf-8">
<title>Vorland Law – Business Card</title>
<link rel="stylesheet" href="https://fonts.googleapis.com/css2?family=Open+Sans:wght@400;600&display=swap">
<style>
  :root {
    --page-bg: #ececec;
    --card-dark: #2b2b2d;
    --panel-grey: #4a4a4c;
    --brand-blue: #3a9cc4;
    --paper: #ffffff;
    --ink: #3a3a3a;
    --muted: #8a8a8a;
    --light-text: #e8e8e8;
  }
  * { margin: 0; padding: 0; box-sizing: border-box; }
  html, body { width: 1200px; height: 818px; overflow: hidden; }
  body {
    position: relative;
    background: var(--page-bg);
    font-family: "Open Sans", Arial, sans-serif;
  }
  .card { position: absolute; background: var(--card-dark); overflow: hidden; }
  .card--front { left: 115px; top: 50px; width: 385px; height: 695px; }
  .card--back  { left: 710px; top: 52px; width: 313px; height: 692px; }

  .firm { position: absolute; left: 0; right: 0; text-align: center; }
  .firm__name { display: block; font-weight: 600; white-space: nowrap; }
  .firm__focus { display: block; font-weight: 400; color: var(--muted); white-space: nowrap; }

  /* Front */
  .front__sheet {
    position: absolute; left: 80px; top: 0; width: 226px; height: 563px;
    background: var(--paper);
    border-radius: 0 0 10px 10px;
  }
  .front__sheet .firm { top: 260px; }
  .front__sheet .firm__name { font-size: 22px; color: var(--ink); }
  .front__sheet .firm__focus { font-size: 9px; margin-top: 4px; }

  .slogans {
    position: absolute; left: 80px; top: 626px; width: 226px; height: 69px;
    background: var(--panel-grey);
    border-radius: 10px 10px 0 0;
    list-style: none;
    padding: 24px 0 0 29px;
  }
  .slogans li {
    position: relative;
    font-size: 8.5px;
    line-height: 13px;
    color: var(--light-text);
    padding-left: 10px;
  }
  .slogans li::before {
    content: ""; position: absolute; left: 0; top: 4px;
    width: 5px; height: 5px; border-radius: 50%;
    background: var(--brand-blue);
  }

  /* Back */
  .back__tab {
    position: absolute; left: 74px; top: 0; width: 219px; height: 46px;
    background: var(--brand-blue);
    border-radius: 0 0 8px 8px;
  }
  .card--back .firm { top: 188px; }
  .card--back .firm__name { font-size: 26px; color: var(--paper); }
  .card--back .firm__focus { font-size: 10px; margin-top: 6px; }

  .person {
    position: absolute; left: 75px; top: 351px; width: 220px; height: 341px;
    background: var(--panel-grey);
    border-radius: 8px 8px 0 0;
    text-align: center;
    padding-top: 27px;
  }
  .person__name { font-size: 21px; font-weight: 400; color: var(--paper); line-height: 28px; }
  .person__title { font-size: 11.5px; color: var(--light-text); }

  .contact__rail {
    position: absolute; left: 62px; top: 435px; width: 55px; height: 210px;
    background: var(--brand-blue);
    border-radius: 8px;
  }
  .contact__icon { position: absolute; left: 12px; width: 30px; height: 30px; }
  .contact__icon--home  { top: 38px; }
  .contact__icon--phone { top: 96px; }
  .contact__icon--web   { top: 155px; }

  .contact__sheet {
    position: absolute; left: 122px; top: 445px; width: 188px; height: 200px;
    background: var(--paper);
    border-radius: 10px;
    padding: 24px 0 0 14px;
    font-size: 8.5px;
    line-height: 12px;
    font-style: normal;
    color: var(--ink);
  }
  .contact__group { margin-bottom: 28px; }
</style>
</head>
<body>

<section class="card card--front" aria-label="Card front">
  <div class="front__sheet">
    <div class="firm">
      <span class="firm__name">Vorland Law</span>
      <span class="firm__focus">Injury &amp; Accident Claims Counsel</span>
    </div>
  </div>
  <ul class="slogans">
    <li>Fight for Full Value.</li>
    <li>Steady Counsel When Harm Is Serious.</li>
  </ul>
</section>

<section class="card card--back" aria-label="Card back">
  <div class="back__tab"></div>
  <div class="firm">
    <span class="firm__name">Vorland Law</span>
    <span class="firm__focus">Injury &amp; Accident Claims Counsel</span>
  </div>

  <div class="person">
    <p class="person__name">Colton R. Vorland</p>
    <p class="person__title">Personal Injury Attorney.</p>
  </div>

  <div class="contact__rail">
    <svg class="contact__icon contact__icon--home" viewBox="0 0 30 30" aria-hidden="true">
      <circle cx="15" cy="15" r="15" fill="#fff"/>
      <path d="M7 15 L15 8 L23 15 H20.5 V22 H17 V17.5 H13 V22 H9.5 V15 Z" fill="var(--brand-blue)"/>
    </svg>
    <svg class="contact__icon contact__icon--phone" viewBox="0 0 30 30" aria-hidden="true">
      <circle cx="15" cy="15" r="15" fill="#fff"/>
      <path d="M8 12 Q8 9 15 9 Q22 9 22 12 L19.5 13 L18.5 11.5 H11.5 L10.5 13 Z" fill="var(--brand-blue)"/>
      <path d="M10 14 H20 L21.5 21 H8.5 Z" fill="var(--brand-blue)"/>
      <circle cx="15" cy="17.5" r="1.8" fill="#fff"/>
    </svg>
    <svg class="contact__icon contact__icon--web" viewBox="0 0 30 30" aria-hidden="true">
      <circle cx="15" cy="15" r="15" fill="#fff"/>
      <rect x="8" y="9" width="14" height="10" rx="1" fill="var(--brand-blue)"/>
      <rect x="9.5" y="10.5" width="11" height="7" fill="#fff"/>
      <rect x="13.5" y="19" width="3" height="2.5" fill="var(--brand-blue)"/>
      <rect x="11" y="21.5" width="8" height="1.5" fill="var(--brand-blue)"/>
    </svg>
  </div>

  <address class="contact__sheet">
    <p class="contact__group">Vorland Law 2140<br>Harbor Crest Avenue Suite<br>410 Bayview, FL 33990</p>
    <p class="contact__group">555.014.2290<br>555.014.7731</p>
    <p>info@vorlandlaw.example<br>www.vorlandlaw.example</p>
  </address>
</section>

</body>
</html>
```